Castvex Equipment Brochure

We require a brochure template that we can use for our equipment.
I have included our logo, a recent ad we ran in a trade magazine and two examples of older brochures.
I have also uploaded some pictures for you to use as you see fit.

Brochure to fit on 11" x 17" folded in half. See old brochures, for example.

Target Market(s)

Industrial manufacturers

Industry/Entity Type

Blow molding and Extrusion Pipes and Profiles

Requirements
Nice to have
• Make use of the red triangle in the logo as part of the corner of the document. To create a connection between the logo and the document.

```html
<!DOCTYPE html>
<html lang="en">
<head>
<meta charset="utf-8">
<title>Castvex Equipment Brochure – Cover</title>
<link rel="stylesheet" href="https://fonts.googleapis.com/css2?family=Montserrat:wght@500;800&family=Roboto+Condensed:wght@700;800&display=swap">
<style>
  :root {
    --backdrop: #dedede;
    --paper: #ffffff;
    --paper-shade: #f1f1f1;
    --brand-navy: #0e2a5c;
    --brand-red: #d3171f;
    --ink-dark: #333333;
    --ink-light: #ffffff;
    --photo-dark: #3a3a3a;
    --photo-mid: #8a8a8a;
    --photo-light: #c9c9c9;
  }
  * { margin: 0; padding: 0; box-sizing: border-box; }
  html, body {
    width: 1200px; height: 1200px; overflow: hidden;
    background: var(--backdrop);
  }
  .cover {
    position: absolute;
    left: 240px; top: 134px;
    width: 720px; height: 932px;
    background: var(--paper);
    overflow: hidden;
    box-shadow: 0 10px 30px rgba(0,0,0,.12);
  }
  .cover-shapes { position: absolute; inset: 0; }
  .brand {
    position: absolute;
    left: 300px; top: 52px;
  }
  .brand-name {
    font-family: "Montserrat", sans-serif;
    font-weight: 800;
    font-size: 64px;
    letter-spacing: 2px;
    color: var(--brand-navy);
    text-transform: uppercase;
    line-height: 1;
  }
  .brand-rule {
    margin-top: 10px;
    width: 340px; height: 2px;
    background: var(--brand-navy);
  }
  .brand-tagline {
    margin-top: 6px;
    font-family: "Montserrat", sans-serif;
    font-weight: 500;
    font-size: 11px;
    letter-spacing: 2.2px;
    color: var(--brand-navy);
    text-transform: uppercase;
  }
  .headline {
    position: absolute;
    left: 150px; top: 690px;
    font-family: "Roboto Condensed", sans-serif;
    font-weight: 800;
    font-size: 74px;
    text-transform: uppercase;
    line-height: .92;
    white-space: nowrap;
  }
  .headline-lead { color: var(--ink-light); display: block; }
  .headline-main { color: var(--ink-dark); display: block; }
  .subline {
    position: absolute;
    left: 152px; top: 848px;
    font-family: "Montserrat", sans-serif;
    font-weight: 500;
    font-size: 17px;
    color: var(--ink-dark);
    white-space: nowrap;
  }
</style>
</head>
<body>
  <main class="cover">
    <svg class="cover-shapes" width="720" height="932" viewBox="0 0 720 932">
      <defs>
        <linearGradient id="machinePhotoTone" x1="0" y1="0" x2="0" y2="1">
          <stop offset="0" stop-color="var(--photo-dark)"/>
          <stop offset=".45" stop-color="var(--photo-mid)"/>
          <stop offset="1" stop-color="var(--photo-light)"/>
        </linearGradient>
      </defs>
      <polygon class="page-shade" points="0,250 330,170 720,170 720,932 0,932" fill="var(--paper-shade)"/>
      <polygon class="corner-triangle" points="24,300 290,300 150,430" fill="var(--brand-red)"/>
      <polygon class="machine-photo" role="img"
               aria-label="Photo of a red blow molding machine on a factory floor"
               points="330,175 720,175 720,790 150,790 150,560"
               fill="url(#machinePhotoTone)"/>
      <rect class="text-band" x="0" y="790" width="720" height="142" fill="var(--paper)"/>
    </svg>

    <header class="brand">
      <div class="brand-name">Castvex</div>
      <div class="brand-rule"></div>
      <div class="brand-tagline">Reliable equipment and service</div>
    </header>

    <h1 class="headline">
      <span class="headline-lead">We sell</span>
      <span class="headline-main">Fix and optimize</span>
    </h1>
    <p class="subline">Your blow mold machine can only produce if it’s running.</p>
  </main>
</body>
</html>
```